Real Estate Agent needs business card design

We have logo designed already, want to have business card designed. Very interested in those smaller size business card as they look very trendy. Business name is called VORENDA REALTY

```html
<!DOCTYPE html>
<html lang="en">
<head>
<meta charset="utf-8">
<title>Vorenda Realty – Business Card</title>
<link href="https://fonts.googleapis.com/css2?family=Arimo:wght@400;700&display=swap" rel="stylesheet">
<style>
  :root {
    --backdrop: #e6e4e1;
    --card: #ffffff;
    --gold: #bf9660;
    --gold-dark: #a88250;
    --ink: #1d1d1d;
    --grey: #5a5a5a;
  }
  * { margin: 0; padding: 0; box-sizing: border-box; }
  html, body {
    width: 1200px; height: 997px; overflow: hidden;
    background: var(--backdrop);
    font-family: "Arimo", Arial, sans-serif;
  }
  .canvas { position: relative; width: 1200px; height: 997px; }
  .card {
    position: absolute;
    width: 520px; height: 300px;
    background: var(--card);
    border-bottom: 7px solid var(--gold);
    box-shadow: 0 10px 30px rgba(0,0,0,0.18);
  }
  .card--front { left: 90px; top: 140px; }
  .card--back { left: 590px; top: 500px; }

  /* Front face */
  .front-brand {
    position: absolute; inset: 0;
    display: flex; align-items: center; justify-content: center; gap: 16px;
  }
  .front-brand__dot {
    width: 34px; height: 34px; border-radius: 50%; background: var(--gold);
  }
  .front-brand__name {
    font-size: 34px; font-weight: 700; letter-spacing: 2px; color: var(--grey);
  }

  /* Back face */
  .badge {
    position: absolute; left: 50%; top: 22px; transform: translateX(-50%);
    width: 112px; height: 112px; border-radius: 50%;
    background: var(--gold);
    display: flex; align-items: center; justify-content: center; text-align: center;
  }
  .badge__name {
    font-size: 13px; font-weight: 700; color: #fff; letter-spacing: 1px; line-height: 1.3;
  }
  .rule {
    position: absolute; top: 150px; height: 1px; background: var(--gold); width: 150px;
  }
  .rule--left { left: 24px; }
  .rule--right { right: 24px; }
  .agent {
    position: absolute; left: 0; right: 0; top: 140px; text-align: center;
  }
  .agent__name {
    font-size: 19px; font-weight: 700; color: var(--gold); letter-spacing: 0.5px;
  }
  .agent__title {
    font-size: 12px; font-weight: 700; color: var(--ink);
  }
  .divider {
    width: 90px; height: 1px; background: var(--gold); margin: 8px auto 8px;
  }
  .icons { display: flex; justify-content: center; gap: 8px; }
  .icons svg { width: 18px; height: 18px; }
  .contact {
    margin-top: 10px; font-size: 13px; color: var(--ink); line-height: 1.55;
  }
  .contact__web {
    font-weight: 700; color: var(--gold-dark); letter-spacing: 0.3px;
  }
</style>
</head>
<body>
<main class="canvas">
  <section class="card card--front" aria-label="Card front">
    <div class="front-brand">
      <span class="front-brand__dot"></span>
      <span class="front-brand__name">VORENDA REALTY</span>
    </div>
  </section>

  <section class="card card--back" aria-label="Card back">
    <div class="badge"><span class="badge__name">VORENDA<br>REALTY</span></div>
    <span class="rule rule--left"></span>
    <span class="rule rule--right"></span>
    <div class="agent">
      <p class="agent__name">ELENA MARSH</p>
      <p class="agent__title">Senior Property Consultant</p>
      <div class="divider"></div>
      <div class="icons">
        <svg viewBox="0 0 18 18" aria-label="Phone"><circle cx="9" cy="9" r="9" fill="#bf9660"/><path d="M6 5c.6 0 1 1.5 1.2 2 .1.4-.6.8-.5 1.1.4.9 1.3 1.8 2.2 2.2.3.1.7-.6 1.1-.5.5.2 2 .6 2 1.2 0 .8-.8 1.5-1.6 1.4C7.6 12.1 5.9 10.4 5.6 6.6 5.5 5.8 5.4 5 6 5z" fill="#fff"/></svg>
        <svg viewBox="0 0 18 18" aria-label="Email"><circle cx="9" cy="9" r="9" fill="#bf9660"/><rect x="4.5" y="6" width="9" height="6.5" fill="none" stroke="#fff" stroke-width="1.2"/><path d="M4.5 6l4.5 3.6L13.5 6" fill="none" stroke="#fff" stroke-width="1.2"/></svg>
        <svg viewBox="0 0 18 18" aria-label="Website"><circle cx="9" cy="9" r="9" fill="#bf9660"/><path d="M7.8 10.2l2.4-2.4M8.6 6.4l1-1a1.8 1.8 0 0 1 2.6 2.6l-1 1M9.4 11.6l-1 1a1.8 1.8 0 0 1-2.6-2.6l1-1" fill="none" stroke="#fff" stroke-width="1.3" stroke-linecap="round"/></svg>
      </div>
      <p class="contact">0400 123 456<br>7C, 48 Harbour Street, Westvale, NSW 2099<br><span class="contact__web">WWW.VORENDAREALTY.COM.AU</span></p>
    </div>
  </section>
</main>
</body>
</html>
```